The Christian Teacher Life-Cycle

Look at the Lifecyle of the Christian School.
Look at the BLT logo.
I am looking for a Christian Teacher Lifecycle that represents the slides in the PP upload.
Our website is bramblewoodlearningtrust.org.
The design should include a summary design showing all four stages, and then four slides representing each of the stages as subsets of the summary design.
When a teacher is going through the Lifecycle, they are going on their Professional Learning Journey that takes 40 years to unfold.
All five should include a copyright 2026 BLT on them.

```html
<!DOCTYPE html>
<html lang="en">
<head>
<meta charset="utf-8">
<title>Stage 1: Focus on "I" – Bramblewood Learning Trust</title>
<link href="https://fonts.googleapis.com/css2?family=Poppins:ital,wght@0,400;0,500;0,600;0,700;1,400&display=swap" rel="stylesheet">
<style>
  :root {
    --blue: #4275ad;
    --blue-dark: #2f5f96;
    --blue-pale: #e3ebf4;
    --grey-text: #6f6f6f;
    --grey-dark: #5e5e5e;
    --tab-grey: #dedede;
    --tab-text: #7a7a7a;
    --page: #ffffff;
    --backdrop: #f2f4f7;
  }
  * { box-sizing: border-box; margin: 0; padding: 0; }
  html, body { width: 1200px; height: 1200px; overflow: hidden; }
  body {
    background: var(--backdrop);
    font-family: "Poppins", sans-serif;
    position: relative;
  }
  .slide {
    position: absolute;
    left: 0; top: 262px;
    width: 1200px; height: 675px;
    background: var(--page);
  }
  .brand { position: absolute; left: 44px; top: 34px; display: flex; align-items: center; gap: 12px; }
  .brand-mark {
    display: flex; align-items: center; gap: 6px;
    color: var(--blue); font-weight: 600; font-size: 22px; width: 66px;
  }
  .brand-mark .dot { width: 10px; height: 10px; border-radius: 50%; background: var(--blue); }
  .brand-name { font-weight: 600; font-size: 15px; color: var(--grey-dark); line-height: 1.2; }
  .brand-tag { font-weight: 600; font-size: 8.2px; color: var(--blue); letter-spacing: 0.1px; margin-top: 2px; }
  .step-pill {
    position: absolute; left: 925px; top: 45px; width: 230px; height: 28px;
    border-radius: 14px; background: var(--blue-pale);
    color: var(--blue-dark); font-weight: 600; font-size: 10.5px;
    display: flex; align-items: center; justify-content: center;
  }
  .stage-tabs { position: absolute; left: 44px; top: 148px; display: flex; gap: 16px; }
  .stage-tab {
    width: 266px; height: 30px; border-radius: 15px;
    background: var(--tab-grey); color: var(--tab-text);
    font-size: 12.6px; display: flex; align-items: center; justify-content: center;
  }
  .stage-tab.active { background: var(--blue); color: #fff; font-weight: 600; }
  .title { position: absolute; left: 44px; top: 208px; font-size: 33px; font-weight: 700; color: var(--blue); line-height: 1.2; }
  .subtitle { position: absolute; left: 44px; top: 257px; font-size: 18px; color: var(--grey-dark); }
  .points { position: absolute; left: 44px; top: 311px; list-style: none; }
  .points li {
    position: relative; padding-left: 22px; height: 26.3px;
    font-size: 13.5px; color: var(--grey-text); line-height: 26px;
  }
  .points li::before {
    content: ""; position: absolute; left: 1px; top: 10px;
    width: 7px; height: 7px; border-radius: 50%; background: var(--blue);
  }
  .photo {
    position: absolute; left: 609px; top: 256px; width: 518px; height: 341px;
    border-radius: 12px; overflow: hidden;
    background: linear-gradient(100deg, #4275ad 0%, #5b86b6 35%, #8a9fb8 65%, #b7b3ad 100%);
  }
  .photo svg { position: absolute; left: 0; bottom: 0; }
  .caption { position: absolute; left: 323px; top: 548px; font-size: 9.4px; font-style: italic; color: var(--grey-text); }
  .rule { position: absolute; left: 0; top: 0; }
  .footer { position: absolute; left: 44px; right: 45px; top: 634px; display: flex; justify-content: space-between; font-size: 8.8px; color: var(--grey-dark); }
  .footer b { font-weight: 600; }
  .footer a { color: var(--blue-dark); font-weight: 500; }
  .footer .motto { font-weight: 500; }
</style>
</head>
<body>
<main class="slide">
  <header class="brand">
    <div class="brand-mark"><span class="dot"></span>BLT</div>
    <div>
      <div class="brand-name">Bramblewood Learning Trust</div>
      <div class="brand-tag">PARTNERSHIP . LEADERSHIP . TRANSFORMATION</div>
    </div>
  </header>
  <div class="step-pill">STEP 01: FOUNDATIONS</div>

  <nav class="stage-tabs">
    <div class="stage-tab active">Stage 1 : The focus is on “I”</div>
    <div class="stage-tab">Stage 2 : Joining CPLC Community</div>
    <div class="stage-tab">Stage 3 : Shared Leadership</div>
    <div class="stage-tab">Stage 4: Invisible Mastery</div>
  </nav>

  <h1 class="title">Stage 1: Focus on “I“</h1>
  <h2 class="subtitle" style="font-weight:400">Early Professional development (Years 0-5)</h2>

  <ul class="points">
    <li>The focus is on “I”</li>
    <li>Fundamental skills dominate such as classroom management</li>
    <li>Curriculum is where I spend my time</li>
    <li>I am a sponge rather than a contributor</li>
    <li>I see myself as a learner</li>
    <li>I reflect on my practice</li>
  </ul>

  <div class="photo" role="img" aria-label="Teacher working on a laptop at a classroom desk with pupils in the background, with a small seedling motif, in a blue tint">
    <svg width="60" height="90" viewBox="0 0 60 90" aria-hidden="true">
      <polygon points="0,0 36,45 0,90" fill="#ffffff"/>
      <polygon points="0,28 12,45 0,62" fill="#4275ad"/>
    </svg>
  </div>

  <p class="caption">Planting roots and Nurturing foundational teaching skills</p>

  <svg class="rule" width="1200" height="620" aria-hidden="true">
    <circle cx="320" cy="597" r="2.2" fill="#4275ad"/>
    <polyline points="320,597 342,597 350,610 1155,610" fill="none" stroke="#4275ad" stroke-width="0.8"/>
  </svg>

  <footer class="footer">
    <span><b>© 2026 BLT .</b> Bramblewood Learning Trust</span>
    <a href="#">bramblewoodlearningtrust.org</a>
    <span class="motto">For Jesus › Through Mission › With Children</span>
  </footer>
</main>
</body>
</html>
```